Poster Needed for Church Conference

I need a poster for a weekend conference at my church. Looking to attract as many people as possible. We are a church in the suburbs of Houston. This is mainly for our own church members but we are opening it up to outside church members.

Please see previous design from last conference and all other graphic work that can (doesn't need to be) included.

Target Market(s)

It's targeted for all people. But our main audience is families. around the age of 30 should be main target.

Industry/Entity Type

Non-Profit

Font styles to use
Serif
Sans Serif

Colors

Designer to choose colors to be used in the design.

Requirements
Must have
• 11x17 design with ability to shrink and blow up. but ideally for 11x17
• Content and wording:
• "Rooted Lantern Conference: Bridging the gap between generations and passing on our deepest beliefs and values."
• Featuring Dr. Glen Marlowe. Author of "The Map of Q9"
• Aug 25-26: Friday 8-10 pm, Saturday 4-8 pm
• Cost Adults $15/Children $5: Covers admission to all sessions and workshops, refreshments and Saturday dinner. *kids 5 and under free
• Childcare provided for all sessions. "
• Please use church logo and address on flyer: 4312 Orchard Bend, Missouri City, TX 77512
Nice to have
• Ideally it will be designed so that we can crop a 16:9 pp announcement slide and header for our website.
Should not have
• anything offensive

```html
<!DOCTYPE html>
<html lang="en">
<head>
<meta charset="utf-8">
<title>Rooted Lantern Conference Poster</title>
<link rel="stylesheet" href="https://fonts.googleapis.com/css2?family=Archivo+Black&family=Open+Sans:wght@400;600&family=Fraunces:opsz,wght@9..144,800&family=Crimson+Text:ital,wght@0,400;0,700;1,400&family=Alfa+Slab+One&display=swap">
<style>
  :root {
    --page: #ffffff;
    --wood-dark: #2b1a10;
    --wood-mid: #4a2f1d;
    --wood-light: #6b4a32;
    --paper: #f1ede4;
    --paper-shade: #ddd6c8;
    --frame: #c9ad7e;
    --frame-dark: #8c6e45;
    --ink: #2a1a10;
    --ink-brown: #4a2c1a;
    --badge-red: #b5161b;
    --badge-red-dark: #7e0d10;
    --cream: #fffaf0;
    --logo-board: #2f2a24;
    --logo-ink: #7cc576;
    --tag-paper: #b98f55;
  }
  * { margin: 0; padding: 0; box-sizing: border-box; }
  html, body { width: 1200px; height: 1200px; overflow: hidden; background: var(--page); }

  .poster {
    position: absolute; left: 148px; top: 0; width: 868px; height: 1200px;
    background:
      repeating-linear-gradient(90deg, rgba(0,0,0,.35) 0 3px, transparent 3px 112px),
      linear-gradient(90deg, var(--wood-dark), var(--wood-mid) 30%, var(--wood-light) 55%, var(--wood-mid) 80%, var(--wood-dark));
    overflow: hidden;
  }
  .shelf {
    position: absolute; left: 0; right: 0; top: 1140px; height: 60px;
    background: linear-gradient(180deg, #6a4a30, #3b2415);
    border-top: 3px solid #24150c;
  }

  .paper {
    position: absolute; left: 44px; top: 62px; width: 780px; height: 870px;
    background: radial-gradient(ellipse at 40% 45%, var(--paper) 55%, var(--paper-shade) 100%);
    box-shadow: 0 6px 18px rgba(0,0,0,.5);
    clip-path: polygon(0 0, 100% 0, 100% 92%, 88% 94%, 76% 92%, 62% 95%, 48% 93%, 34% 96%, 20% 93%, 8% 95%, 0 93%);
  }

  .photo-frame {
    position: absolute; background: var(--frame); padding: 22px;
    box-shadow: 0 4px 12px rgba(0,0,0,.55);
    border: 2px solid var(--frame-dark);
  }
  .logo-frame { left: 40px; top: 96px; width: 384px; height: 344px; transform: rotate(1.5deg); }
  .crowd-frame { left: 404px; top: 104px; width: 410px; height: 344px; transform: rotate(-3deg); }
  .logo-board {
    width: 100%; height: 100%; background: var(--logo-board);
    display: flex; align-items: center; justify-content: center; gap: 10px;
  }
  .logo-mark { width: 16px; height: 16px; background: var(--logo-ink); }
  .logo-name {
    font-family: "Open Sans", sans-serif; font-weight: 600; font-size: 20px;
    color: var(--logo-ink); letter-spacing: 1px; line-height: 1.2;
  }
  .crowd-photo {
    width: 100%; height: 100%;
    background: linear-gradient(100deg, #2a4fa8 0%, #3a3550 35%, #b8475a 65%, #d9cfc2 100%);
  }

  .title {
    position: absolute; left: 44px; width: 780px; text-align: center;
    font-family: "Archivo Black", sans-serif; color: var(--ink);
    text-shadow: 1px 2px 0 rgba(120,80,40,.5);
  }
  .title-main { top: 484px; font-size: 66px; letter-spacing: -2px; line-height: 1; }
  .title-sub { top: 566px; font-size: 48px; letter-spacing: -1px; line-height: 1; }

  .divider { position: absolute; left: 228px; top: 642px; width: 412px; height: 20px; }

  .address {
    position: absolute; left: 44px; width: 780px; top: 680px; text-align: center;
    font-family: "Open Sans", sans-serif; font-size: 22px; color: var(--ink); letter-spacing: -.3px;
  }
  .tagline {
    position: absolute; left: 90px; width: 700px; top: 736px; text-align: center;
    font-family: "Fraunces", serif; font-weight: 800; font-size: 24px; line-height: 1.15;
    color: var(--ink-brown); text-shadow: 1px 1px 0 rgba(0,0,0,.15);
  }

  .featuring-tag {
    position: absolute; left: 96px; top: 888px; width: 244px; height: 232px;
    background: linear-gradient(160deg, #cfa869, var(--tag-paper));
    transform: rotate(-4deg); box-shadow: 0 4px 10px rgba(0,0,0,.5);
  }
  .featuring-text {
    position: absolute; left: 108px; top: 942px; z-index: 3;
    font-family: "Alfa Slab One", serif; font-size: 18px; line-height: 1.4;
    color: var(--cream); transform: rotate(8deg); transform-origin: left top;
    text-shadow: 1px 1px 0 rgba(0,0,0,.5); white-space: nowrap;
  }

  .speaker-frame {
    position: absolute; left: 326px; top: 888px; width: 228px; height: 228px;
    background: var(--cream); padding: 14px 14px 28px;
    transform: rotate(2deg); box-shadow: 0 4px 12px rgba(0,0,0,.55);
  }
  .speaker-photo { width: 100%; height: 100%; background: linear-gradient(180deg, #141210, #4a3a30); }

  .date-badge {
    position: absolute; left: 524px; top: 800px; width: 272px; height: 272px; border-radius: 50%;
    background: radial-gradient(circle at 40% 35%, var(--badge-red), var(--badge-red-dark));
    border: 8px solid var(--cream); box-shadow: 0 4px 12px rgba(0,0,0,.4);
    display: flex; flex-direction: column; align-items: center; justify-content: center;
    color: var(--cream); text-align: center; font-family: "Crimson Text", serif; line-height: 1.1;
    z-index: 2;
  }
  .badge-date { font-size: 31px; }
  .badge-day { font-size: 30px; }
  .badge-time { font-family: "Alfa Slab One", serif; font-size: 20px; margin-bottom: 4px; }
  .badge-price { font-size: 20px; }

  .footnotes {
    position: absolute; left: 0; width: 868px; top: 1104px; text-align: center; z-index: 4;
    font-family: "Crimson Text", serif; font-style: italic; font-size: 24px; line-height: 1.3;
    color: var(--cream); text-shadow: 1px 1px 2px #000, -1px -1px 1px #000;
  }
</style>
</head>
<body>
  <main class="poster">
    <div class="shelf"></div>
    <div class="paper"></div>

    <div class="photo-frame logo-frame">
      <div class="logo-board">
        <span class="logo-mark"></span>
        <span class="logo-name">cedar hollow<br>community church</span>
      </div>
    </div>
    <div class="photo-frame crowd-frame">
      <div class="crowd-photo" role="img" aria-label="Photo of a congregation standing in worship with raised hands"></div>
    </div>

    <h1 class="title title-main">ROOTED LANTERN</h1>
    <h2 class="title title-sub">CONFERENCE</h2>

    <svg class="divider" viewBox="0 0 412 20" aria-hidden="true">
      <line x1="0" y1="10" x2="180" y2="10" stroke="#2a1a10" stroke-width="1.5"/>
      <circle cx="206" cy="10" r="5" fill="#2a1a10"/>
      <line x1="232" y1="10" x2="412" y2="10" stroke="#2a1a10" stroke-width="1.5"/>
    </svg>

    <p class="address">4312 ORCHARD BEND, MISSOURI CITY, TX 77512</p>
    <p class="tagline">Bridging the gap between generations and passing on our deepest beliefs and values”</p>

    <div class="featuring-tag"></div>

    <div class="speaker-frame">
      <div class="speaker-photo" role="img" aria-label="Portrait photo of the featured speaker"></div>
    </div>

    <p class="featuring-text">FEATURING<br>DR. GLEN MARLOWE<br>AUTHOR OF<br>“THE MAP OF Q9”</p>

    <div class="date-badge">
      <span class="badge-date">August 25-26</span>
      <span class="badge-day">Friday</span>
      <span class="badge-time">8pm - 10pm</span>
      <span class="badge-day">Saturday</span>
      <span class="badge-time">4pm - 8pm</span>
      <span class="badge-price">$15 Adult</span>
      <span class="badge-price">$5 Children</span>
    </div>

    <p class="footnotes">
      Cost Covers to all sessions and workshops , refreshments and Saturday dinner<br>
      *Kids 5 and under free<br>
      “Childcare provided for all sessions.”
    </p>
  </main>
</body>
</html>
```